Flyer für Beratung, Planung und Montage von Photovoltaikanlagen, Wallboxen usw.
Der Ablauf war optimal. Auf Änderungswünsche wurde umgehend eingegangen. Die Bearbeitung erfolgt sehr zeitnah. Wir sind sehr zufrieden und können TOLVERIKO nur empfehlen.
Zielgruppe
Individuelle Beratung, Planung und Montage von Photovoltaikanlagen, Wallboxen, Balkonkraftwerke, PowerToHeat, Stromspeicher etc., (Neuanlagen & Bestandsanlagen), Privat- & Firmenkunden
Aufgabenstellung
Qualitativ hochwertige Markenprodukte, Seriös, Modern, Regionaler Anbieter, Flyer für gezielte regionale Verteilung (Briefkasten)

```html
<!DOCTYPE html>
<html lang="de">
<head>
<meta charset="utf-8">
<title>Flusswerk – Ihr regionaler Anbieter für erneuerbare Energien</title>
<link rel="stylesheet" href="https://fonts.googleapis.com/css2?family=Montserrat:wght@800&family=Nunito:wght@800;900&family=Didact+Gothic&display=swap">
<style>
  :root{
    --lime:#d2e600;
    --lime-soft:rgba(214,236,40,0.88);
    --ink:#3b4345;
    --panel:#4a5355;
    --card:#ffffff;
    --page:#eceeed;
    --black:#000000;
  }
  *{box-sizing:border-box;margin:0;padding:0}
  html,body{width:849px;height:1200px;overflow:hidden;background:var(--page)}
  .flyer{position:relative;width:849px;height:1200px;overflow:hidden;background:var(--page);font-family:"Didact Gothic",sans-serif;color:var(--ink)}
  .abs{position:absolute}
  .hero-photo{left:0;top:0;width:849px;height:522px;background:linear-gradient(160deg,#e9ecee 0%,#bfc4c8 30%,#6b6f72 55%,#8a6a4c 80%,#5b4d3a 100%)}
  .band-lime{left:0;top:888px;width:849px;height:232px;background:var(--lime)}
  .footer{left:0;top:1119px;width:849px;height:81px;background:var(--black);color:#fff}
  .brand{display:flex;align-items:center;gap:6px;font-family:"Montserrat",sans-serif;font-weight:800;letter-spacing:1px;white-space:nowrap}
  .brand-top{right:16px;top:58px;font-size:17px;color:var(--ink)}
  .brand-mark{width:14px;height:14px;background:var(--lime)}
  .intro{left:0;top:100px;width:743px;height:302px;background:var(--lime-soft);padding:22px 20px 0 48px}
  .intro h1{font-family:"Montserrat",sans-serif;font-weight:800;font-size:34px;line-height:41px;letter-spacing:0.3px;color:var(--ink)}
  .intro p{margin-top:14px;font-size:21.2px;line-height:27.7px;color:var(--ink);white-space:nowrap}
  .services-label{left:22px;top:427px;width:271px;height:64px;background:var(--card);border-radius:6px;text-align:center;font-family:"Nunito",sans-serif;font-weight:900;font-size:27px;line-height:32px;padding-top:1px}
  .card{background:var(--card);border-radius:6px}
  .photo{border-radius:8px}
  .card-title{font-family:"Nunito",sans-serif;font-weight:800;color:var(--ink);text-align:center}
  .storage{left:25px;top:506px;width:250px;height:407px}
  .storage .photo{left:62px;top:14px;width:126px;height:316px;background:linear-gradient(90deg,#1c1d1e,#3b3e40 55%,#16181a);border-radius:4px}
  .storage .card-title{left:0;top:345px;width:250px;font-size:18px}
  .storage .card-sub{left:0;top:372px;width:250px;text-align:center;font-size:14px;line-height:16px}
  .pv{left:299px;top:430px;width:525px;height:239px}
  .pv .photo{left:17px;top:15px;width:489px;height:196px;background:linear-gradient(180deg,#d9dde0 0%,#3a3f45 45%,#8d6a45 85%,#4f5a3a 100%)}
  .pv .card-title{left:18px;top:214px;font-size:19px;text-align:left}
  .pv .card-note{right:18px;top:217px;font-size:15.5px}
  .charge{left:299px;top:684px;width:251px;height:226px}
  .charge .photo{left:9px;top:11px;width:233px;height:148px;background:linear-gradient(120deg,#c7ced3 0%,#7b7f82 45%,#e9eaea 80%,#f7f7f7 100%)}
  .service{left:574px;top:684px;width:250px;height:226px}
  .service .photo{left:8px;top:9px;width:233px;height:148px;background:linear-gradient(180deg,#eef2f6 0%,#c9d3df 55%,#2d4a78 100%)}
  .charge .card-title,.service .card-title{left:0;top:176px;width:100%;font-size:18px;line-height:23.5px}
  .service .card-title{top:175px}
  .cta-text{left:0;top:940px;width:424px;height:137px;background:var(--card);padding:4px 0 0 47px;font-family:"Nunito",sans-serif;font-weight:800;font-size:24px;line-height:31px}
  .contact{left:451px;top:946px;width:369px;height:120px;background:var(--panel);border:2px solid #fff;border-radius:6px;color:#fff}
  .contact-head{left:-2px;top:-2px;width:369px;height:45px;border:2px solid #fff;border-radius:6px;background:var(--panel);text-align:center;font-family:"Nunito",sans-serif;font-weight:800;font-size:24px;line-height:40px}
  .contact-icon{left:10px;top:56px;width:46px;height:46px}
  .contact-lead{left:61px;top:50px;font-size:22px}
  .contact-phone{left:61px;top:76px;font-family:"Nunito",sans-serif;font-weight:900;font-size:25px;letter-spacing:0.3px;white-space:nowrap}
  .brand-foot{left:48px;top:1166px;font-size:11px;letter-spacing:0.5px;gap:5px;color:#fff}
  .brand-foot .brand-mark{width:11px;height:11px}
  .footer-head{left:158px;top:1138px;font-family:"Nunito",sans-serif;font-weight:800;font-size:15.5px;color:#fff}
  .footer-links{left:158px;top:1163px;font-size:15.5px;display:flex;gap:16px;color:#fff;white-space:nowrap}
  .footer-links a{color:#fff}
</style>
</head>
<body>
<div class="flyer">
  <div class="abs hero-photo" role="img" aria-label="Foto: modernes Einfamilienhaus mit Photovoltaikmodulen auf dem Dach"></div>
  <div class="abs band-lime"></div>

  <div class="abs brand brand-top"><span class="brand-mark"></span>FLUSSWERK</div>

  <section class="abs intro">
    <h1>IHR REGIONALER ANBIETER FÜR<br>ERNEUERBARE ENERGIEN</h1>
    <p>Wir sind Ihre regionalen Experten für maßgeschneiderte<br>Photovoltaik- und Stromspeicherlösungen. Egal, ob Sie Privat- oder<br>Gewerbekunde sind. Wir bieten passgenaue Lösungen und 360°<br>Service für Ihre individuellen Bedürfnisse – und das sowohl für Neu-<br>als auch Bestandsanlagen. Von der detaillierten Planung bis zur<br>professionellen Installation und darüber hinaus.</p>
  </section>

  <div class="abs services-label">UNSERE<br>LEISTUNGEN:</div>

  <article class="abs card storage">
    <div class="abs photo" role="img" aria-label="Produktfoto: schwarzer Heimstromspeicher im Standgehäuse"></div>
    <h2 class="abs card-title">Stromspeicher</h2>
    <p class="abs card-sub">Erweiterung, Nachrüstung,<br>Hersteller</p>
  </article>

  <article class="abs card pv">
    <div class="abs photo" role="img" aria-label="Foto: Wohnhaus mit Photovoltaikanlage auf dem Dach in der Abenddämmerung"></div>
    <h2 class="abs card-title">Photovoltaikanlage</h2>
    <p class="abs card-note">360° Service rund um ihre PV-Anlage</p>
  </article>

  <article class="abs card charge">
    <div class="abs photo" role="img" aria-label="Foto: Elektroauto lädt an einer Wallbox vor einem modernen Haus"></div>
    <h2 class="abs card-title">Ladeinfrastruktur<br>und Elektromobilität</h2>
  </article>

  <article class="abs card service">
    <div class="abs photo" role="img" aria-label="Foto: Holzwürfel auf Solarmodul, ein Finger wählt den zufriedenen Würfel"></div>
    <h2 class="abs card-title">Wartung - Service<br>und Monitoring</h2>
  </article>

  <div class="abs cta-text">Starten Sie jetzt Ihre ganz persönliche Energiewende und Vereinbaren Sie noch heute einen kostenfreien</div>

  <div class="abs contact">
    <div class="abs contact-head">Kostenlose Beratung</div>
    <svg class="abs contact-icon" viewBox="0 0 24 24" aria-hidden="true"><path fill="#fff" d="M6.6 2.2c.6-.3 1.3-.1 1.6.5l2 3.6c.3.6.2 1.3-.3 1.7L8.3 9.4c1.1 2.5 3.2 4.8 5.8 6.2l1.5-1.6c.5-.5 1.2-.6 1.8-.2l3.4 2.2c.6.4.8 1.1.4 1.7l-1.3 2.3c-.6 1-1.8 1.5-3 1.2C9.8 19.5 4.3 14 2.7 6.9c-.3-1.2.2-2.4 1.2-3z"/></svg>
    <div class="abs contact-lead">Kontaktiere uns jetzt!</div>
    <div class="abs contact-phone">+49 (0)8231 – 4470120</div>
  </div>

  <footer class="abs footer"></footer>
  <div class="abs brand brand-foot"><span class="brand-mark"></span>FLUSSWERK</div>
  <div class="abs footer-head">Finde mehr heraus</div>
  <div class="abs footer-links">
    <a href="#">https://flusswerk-energie.de/</a>
    <span>Tel : +49 (0)8231 – 4470120</span>
    <span>Mail : info@flusswerk-energie.de</span>
  </div>
</div>
</body>
</html>
```